New Massage Business needs a Card design

We need a card design for our new massage therapy business based in Sydney, Au. The business is getting a makeover, so a little later on we'll need shirts, various pamphlets and promotional flyers, and possibly a website. The winner will be offered those jobs as well.

Colour scheme should be green, black, and steel/charcoal grey. The business focuses on massage as an anatomical solution to stress, muscle aches, pains and fatigue. Ideally we'd like an anatomical image of the muscle system (ref to the attached files). In my mind this image takes up most of the left third of the card, and shows points of tension and pain at the neck and lower back. This image should be the grey portion of the card.

On the upper right is the other image attached, with a simple line drawing of a vehicle on the left end of the line, and a building on the right end replacing the stick figure (we have a therapist specializing in mobile massage). The blank part in the middle of the line should have "Vital Bodyworks", and in smaller writing below, "The Tension Fix".

Bottom right corner should have the contact and business details.
On the back we'd like a "next appointment" and "refer a friend" option.

If you have a design which doesn't fit the above, but you feel suits the business, please submit anyway - sometimes you don't know what you like until you see it.

Business Details:
Name: Vital Bodyworks - The Tension Fix

Massage Therapy

Business Details:
Contact name: Marcus
Title: Massage Therapist
Contact: 0458203167
Email: info@qlbrelief.example

Requirements
Must have
• Colour scheme should be green, black, and steel/charcoal grey. The business focuses on massage as an anatomical solution to stress, muscle aches, pains and fatigue. Ideally we'd like an anatomical image of the muscle system (ref to the attached files). In my mind this image takes up most of the left third of the card, and shows points of tension and pain at the neck and lower back. This image should be the grey portion of the card.
• On the upper right is the other image attached, with a simple line drawing of a vehicle on the left end of the line, and a building on the right end replacing the stick figure (we have a therapist specializing in mobile massage). The blank part in the middle of the line should have "Vital Bodyworks", and in smaller writing below, "The Tension Fix".
• Bottom right corner should have the contact and business details.
• On the back we'd like a "next appointment" and "refer a friend" option.
Nice to have
• Matt finish - no gloss
• If you have a design which doesn't fit the above, but you feel suits the business, please submit anyway - sometimes you don't know what you like until you see it.
Should not have
• Anything 'Zen'. The business promotes the physiological and scientific benefits of massage. For clients with spiritual or meditative needs, we refer out.

```html
<!DOCTYPE html>
<html lang="en">
<head>
<meta charset="utf-8">
<title>Vital Bodyworks – Business Card</title>
<link rel="stylesheet" href="https://fonts.googleapis.com/css2?family=Source+Sans+3:wght@400;600;700&display=swap">
<style>
  :root {
    --canvas-bg: #c9c9c9;
    --card-green: #c2e853;
    --charcoal: #2b2b2b;
    --steel: #474a4c;
    --muscle-grey: #4a4b4c;
  }
  * { box-sizing: border-box; margin: 0; padding: 0; }
  html, body {
    width: 1200px;
    height: 1000px;
    overflow: hidden;
  }
  body {
    position: relative;
    background: var(--canvas-bg);
    font-family: "Source Sans 3", "Helvetica Neue", Arial, sans-serif;
    color: var(--charcoal);
  }
  .card {
    position: absolute;
    width: 735px;
    height: 420px;
    background: var(--card-green);
    overflow: hidden;
  }
  .card--front { left: 110px; top: 42px; }
  .card--back  { left: 343px; top: 526px; }

  /* Front */
  .anatomy-art {
    position: absolute;
    left: 0;
    top: 0;
    width: 340px;
    height: 420px;
    background: linear-gradient(90deg, var(--muscle-grey) 0%, #6f7a5a 55%, var(--card-green) 100%);
  }
  .brand-mark {
    position: absolute;
    right: 115px;
    top: 52px;
    text-align: center;
    font-weight: 600;
    color: var(--steel);
    line-height: 1.1;
  }
  .brand-mark__name { font-size: 17px; }
  .brand-mark__tagline { font-size: 9px; }

  .contact {
    position: absolute;
    right: 55px;
    top: 222px;
    text-align: right;
    color: var(--charcoal);
  }
  .contact__name {
    font-size: 36px;
    font-weight: 700;
    line-height: 1.1;
  }
  .contact__title {
    font-size: 26px;
    font-weight: 400;
    line-height: 1.15;
    margin-bottom: 18px;
  }
  .contact__line {
    font-size: 21px;
    font-weight: 400;
    line-height: 1.25;
    letter-spacing: 0.3px;
  }

  /* Back */
  .field-label {
    position: absolute;
    left: 54px;
    font-size: 21px;
    font-weight: 400;
    color: var(--steel);
  }
  .field-label--appointment { top: 50px; }
  .field-label--referral { top: 288px; }

  .back-brand {
    position: absolute;
    left: 0;
    right: 0;
    top: 172px;
    text-align: center;
    font-weight: 600;
    color: var(--steel);
    line-height: 1.1;
  }
  .back-brand__name { font-size: 36px; }
  .back-brand__tagline { font-size: 18px; }
</style>
</head>
<body>
  <section class="card card--front" aria-label="Business card front">
    <div class="anatomy-art" role="img" aria-label="Charcoal grey illustration of the back and shoulder muscles of a human torso"></div>

    <div class="brand-mark">
      <div class="brand-mark__name">Vital Bodyworks</div>
      <div class="brand-mark__tagline">The Tension Fix</div>
    </div>

    <div class="contact">
      <div class="contact__name">Marcus</div>
      <div class="contact__title">Massage Therapist</div>
      <div class="contact__line">0458203167</div>
      <div class="contact__line">info@qlbrelief.example</div>
    </div>
  </section>

  <section class="card card--back" aria-label="Business card back">
    <div class="field-label field-label--appointment">Next appointment:</div>

    <div class="back-brand">
      <div class="back-brand__name">Vital Bodyworks</div>
      <div class="back-brand__tagline">The Tension Fix</div>
    </div>

    <div class="field-label field-label--referral">Refer a friend:</div>
  </section>
</body>
</html>
```